Mendwell47 Business Card Redesign

I want to create a design for brand new business cards, I need something exceptional for clear plastic business card design. Please do not submit without it being on a clear design. Photos of the various logo versions attached.

```html
<!DOCTYPE html>
<html lang="en">
<head>
<meta charset="utf-8">
<title>Mendwell47 Business Card</title>
<link rel="stylesheet" href="https://fonts.googleapis.com/css2?family=Montserrat:wght@500;600;700&display=swap">
<style>
  :root {
    --page-bg: #e6e1d9;
    --card-top: #f4efe6;
    --card-bottom: #ebe3d4;
    --card-edge: rgba(255, 255, 255, 0.85);
    --navy: #223a63;
    --navy-deep: #1a2d4f;
    --gold: #c9a24f;
    --gold-light: #e2c27a;
    --ink: #3a3a3a;
    --band-text: #e8ebf2;
  }
  * { margin: 0; padding: 0; box-sizing: border-box; }
  html, body {
    width: 1200px;
    height: 1047px;
    overflow: hidden;
    background: var(--page-bg);
    font-family: "Montserrat", sans-serif;
  }
  .business-card {
    position: absolute;
    left: 80px;
    top: 241px;
    width: 1040px;
    height: 565px;
    border-radius: 24px;
    overflow: hidden;
    background: linear-gradient(160deg, var(--card-top), var(--card-bottom));
    box-shadow: 0 0 0 2px var(--card-edge), 0 18px 40px rgba(60, 50, 35, 0.18);
  }
  .card-shapes {
    position: absolute;
    inset: 0;
    width: 1040px;
    height: 565px;
  }
  .name-bar {
    position: absolute;
    left: 6px;
    top: 89px;
    width: 21px;
    height: 79px;
    background: var(--gold);
  }
  .holder-name {
    position: absolute;
    left: 44px;
    top: 88px;
    font-size: 40px;
    font-weight: 700;
    letter-spacing: 1px;
    color: var(--gold);
    text-transform: uppercase;
  }
  .holder-title {
    position: absolute;
    left: 44px;
    top: 138px;
    font-size: 25px;
    font-weight: 500;
    letter-spacing: 0.5px;
    color: var(--ink);
  }
  .brand {
    position: absolute;
    right: 46px;
    top: 248px;
    display: flex;
    align-items: center;
    gap: 18px;
  }
  .brand-dot {
    width: 40px;
    height: 40px;
    border-radius: 50%;
    background: var(--navy);
  }
  .brand-name {
    font-size: 56px;
    font-weight: 700;
    color: var(--gold);
    letter-spacing: 1px;
  }
  .contact-list {
    position: absolute;
    left: 38px;
    top: 414px;
    list-style: none;
  }
  .contact-item {
    display: flex;
    align-items: center;
    gap: 14px;
    height: 40px;
    font-size: 25px;
    font-weight: 500;
    color: var(--band-text);
    letter-spacing: 0.4px;
  }
  .contact-icon {
    width: 22px;
    height: 22px;
    flex: none;
  }
  .service-areas {
    position: absolute;
    left: 649px;
    top: 416px;
    font-size: 25px;
    line-height: 40px;
    letter-spacing: 0.4px;
  }
  .service-heading {
    font-weight: 600;
    color: var(--gold-light);
  }
  .service-line {
    font-weight: 500;
    color: var(--band-text);
  }
</style>
</head>
<body>
  <article class="business-card">
    <svg class="card-shapes" viewBox="0 0 1040 565" aria-hidden="true">
      <defs>
        <linearGradient id="band-fill" x1="0" y1="0" x2="1" y2="1">
          <stop offset="0" stop-color="var(--navy)"/>
          <stop offset="1" stop-color="var(--navy-deep)"/>
        </linearGradient>
        <linearGradient id="swoosh-fill" x1="0" y1="0" x2="1" y2="0">
          <stop offset="0" stop-color="var(--gold-light)"/>
          <stop offset="1" stop-color="var(--gold)"/>
        </linearGradient>
      </defs>
      <path d="M0,333 C300,318 700,350 1040,452 L1040,565 L0,565 Z" fill="url(#band-fill)"/>
      <path d="M0,320 C300,304 700,334 1040,428 L1040,446 C700,350 300,320 0,330 Z" fill="url(#swoosh-fill)"/>
    </svg>

    <div class="name-bar"></div>
    <h1 class="holder-name">Owen Carlisle</h1>
    <p class="holder-title">Managing Director</p>

    <div class="brand">
      <span class="brand-dot"></span>
      <span class="brand-name">Mendwell47</span>
    </div>

    <ul class="contact-list">
      <li class="contact-item">
        <svg class="contact-icon" viewBox="0 0 24 24" aria-hidden="true">
          <path d="M3 9c0-3 4-5 9-5s9 2 9 5v2h-5V9H8v2H3z M6 12h12l2 8H4z" fill="var(--band-text)"/>
        </svg>
        (833) MEND-470
      </li>
      <li class="contact-item">
        <svg class="contact-icon" viewBox="0 0 24 24" aria-hidden="true">
          <rect x="2" y="5" width="20" height="14" rx="1.5" fill="var(--band-text)"/>
          <path d="M3 6l9 7 9-7" fill="none" stroke="var(--navy)" stroke-width="1.8"/>
        </svg>
        info@mendwell-47.com
      </li>
      <li class="contact-item">
        <svg class="contact-icon" viewBox="0 0 24 24" aria-hidden="true">
          <circle cx="12" cy="12" r="10" fill="var(--band-text)"/>
          <path d="M2 12h20 M12 2c-4 4-4 16 0 20 M12 2c4 4 4 16 0 20" fill="none" stroke="var(--navy)" stroke-width="1.5"/>
        </svg>
        mendwell-47.com
      </li>
    </ul>

    <div class="service-areas">
      <p class="service-heading">Service Areas</p>
      <p class="service-line">Serving clients nationwide</p>
      <p class="service-line">All 50 states covered</p>
    </div>
  </article>
</body>
</html>
```